Wordpress website design for a high-end painting business

We are currently rebranding and are looking to update our Wordpress theme. We have recently rebranded our logo on PixelHarbor, and would like our website to be equally as refined.
Our business is named “Kestrel Painters”. We are a high-end painting business that is known for being professional and having high standards. Our clean and professional image is important as it separates us from our competition. Our current website can be found at www.wrenfieldcoatings.co.nz . We designed the site ourselves so it is understandably rudimentary. We are generally happy with the. page layout of our existing site, but we like a professional remodel. Any ideas on improvement welcomed.
We would like the front page of the website to summarise all of the info throughout the whole website (I.e introduction, photos, testimonials, contact info etc.) as visitors typically scroll through the first page to see that we are reputable and get to our contact number/email contact at the bottom of the page. We would like this first page to give a clean well rounded image of our business. We would like the gallery to be a scroll through of large photos, as it is difficult to see paint details in smaller photos. A contact page with an enquiry section would also be good.
For the colour scheme, we would like something that fits a bold, masculine and high end theme (similar to our logo attached).
We would like the footer to include Veltora paint logos and the accredited painter logo we have included as these are important to our profession.
We have attached some photos of our work also. I will add more in the coming days. More can also be found on our website.
If you have questions or comments, please don’t hesitate to ask and I will get back as soon as possible.
We are open to your own interpretation or ideas for a better layout/site provided they fit the general brief of being a well rounded site for our profession.
Thanks,
Kestrel Painters.
Target Market(s)
High end clients
Industry/Entity Type
Painting (interior and exterior)
Coding
Coded - Design and coding required
Requirements
Must have
- Classy feel, separating us from typical painting companies. Well rounded homepage.
Nice to have
- Lots of examples of our work
Should not have
- Untidy paint motifs (eg, paint droplets, paint splashes)

```html
<!DOCTYPE html>
<html lang="en">
<head>
<meta charset="utf-8">
<title>Kestrel Painters — Always on Target</title>
<link rel="stylesheet" href="https://fonts.googleapis.com/css2?family=Roboto+Slab:wght@300;400;500&display=swap">
<style>
:root{
  --brown:#8a6a45;
  --brown-dark:#6f5434;
  --cream:#fcf5ee;
  --field:#e8dcc9;
  --ink:#2b2b2b;
  --muted:#6b6b6b;
  --white:#ffffff;
  --night:#23272c;
  --rule:#e2d6c6;
}
*{box-sizing:border-box;margin:0;padding:0}
html,body{width:1200px;height:4205px;overflow:hidden}
body{font-family:"Roboto Slab",Georgia,serif;color:var(--ink);background:var(--white);position:relative}
section,header,footer{position:relative;width:1200px}
.abs{position:absolute}
.ico{display:inline-flex;align-items:center;justify-content:center;border-radius:50%;border:1.5px solid var(--brown);color:var(--brown)}
.ico svg{width:14px;height:14px}

/* hero */
.hero{height:720px;overflow:hidden}
.hero-photo{position:absolute;inset:0;background:linear-gradient(180deg,#5b6f8a 0%,#8a8c8a 35%,#7d6b57 60%,#4f5a3a 85%,#3d4a2c 100%)}
.hero-shade{position:absolute;inset:0;background:rgba(20,25,35,.28)}
.nav{position:absolute;top:34px;font-size:12.5px;letter-spacing:2px;color:var(--white);display:flex;gap:30px}
.nav-left{left:85px}
.nav-right{left:788px}
.nav-phone{position:absolute;left:1081px;top:25px;width:34px;height:34px;border-color:var(--white);color:var(--white)}
.brand-badge{position:absolute;left:486px;top:-42px;width:228px;height:228px;border-radius:50%;background:var(--white);display:flex;align-items:flex-end;justify-content:center;padding-bottom:38px}
.brand-name{font-size:19px;font-weight:500;color:var(--brown-dark);letter-spacing:1px;text-transform:uppercase;text-align:center;line-height:1.2}
.hero-title{position:absolute;top:342px;width:100%;text-align:center;font-size:52px;font-weight:400;color:var(--white)}
.hero-text{position:absolute;top:420px;width:100%;text-align:center;font-size:15.5px;line-height:23px;color:var(--white);font-weight:300}
.btn{display:inline-flex;align-items:center;justify-content:center;border-radius:22px;font-size:12px;letter-spacing:2.5px;font-weight:500;text-transform:uppercase}
.btn-light{position:absolute;left:494px;top:482px;width:212px;height:42px;background:var(--white);color:var(--brown)}

/* services */
.services{height:1008px}
.services-title{position:absolute;top:794px;}
.section-title{font-size:36px;font-weight:400;line-height:43px;text-align:center}
.lead{font-size:14px;line-height:23px;color:var(--muted);text-align:center;font-weight:300}
.service{position:absolute;width:300px;text-align:center}
.service-photo{width:237px;height:237px;border-radius:50%;margin:0 auto;box-shadow:0 0 0 6px #f3efe9}
.service-name{margin-top:22px;font-size:18px;line-height:22px}
.learn{position:absolute;left:522px;top:1103px;width:156px;height:40px;background:var(--brown);color:var(--white)}

/* pride */
.pride{height:581px;background:var(--cream);overflow:hidden}
.pride-photo{position:absolute;left:-20px;top:0;width:567px;height:581px;border-radius:0 290px 290px 0;background:linear-gradient(180deg,#a9c0d6 0%,#d8d2b8 40%,#b7ad8a 62%,#6f8f3e 80%,#55762f 100%)}
.pride-copy{position:absolute;left:616px;top:85px;width:430px}
.pride-copy h2{font-size:36px;font-weight:400;line-height:43px;margin-bottom:28px}
.pride-copy p{font-size:14px;line-height:22.5px;color:var(--muted);font-weight:300;margin-bottom:22px}
.btn-brown{background:var(--brown);color:var(--white)}
.call{display:flex;align-items:center;gap:12px}
.call .ico{width:32px;height:32px}
.call small{display:block;font-size:11.5px;color:var(--ink)}
.call strong{display:block;font-size:24px;font-weight:400;color:var(--brown);line-height:28px}

/* feedback */
.feedback{height:448px;background:var(--brown);color:var(--white)}
.feedback .section-title{position:absolute;top:70px;width:100%}
.quote-card{position:absolute;top:189px;width:427px;height:200px;border:1px solid rgba(255,255,255,.45);border-radius:8px;padding:44px 26px 0}
.quote-mark{position:absolute;left:26px;top:-19px;width:38px;height:38px;border-radius:50%;background:#e8dcc9;display:flex;align-items:center;justify-content:center}
.quote-card p{font-size:14px;line-height:22.5px;font-weight:300}
.quote-card cite{display:block;margin-top:18px;font-style:normal;font-size:13px;font-weight:300}
.quote-card cite b{font-weight:500}
.slide-arrow{position:absolute;top:2580px}

/* projects */
.projects{height:463px}
.projects h2{position:absolute;left:157px;top:63px;font-size:36px;font-weight:400}
.project{position:absolute;top:146px;height:294px}
.arrows{position:absolute;left:1016px;top:80px;display:flex;gap:12px}

/* contact */
.enquiry{height:523px;background:var(--cream);overflow:hidden}
.enquiry .kicker{position:absolute;left:157px;top:90px;font-size:16px}
.enquiry h2{position:absolute;left:157px;top:118px;font-size:34px;font-weight:400}
.enquiry .intro{position:absolute;left:603px;top:88px;width:445px;font-size:14px;line-height:22.5px;color:var(--muted);font-weight:300}
.field{position:absolute;background:var(--field);border-radius:8px;font-size:13px;color:var(--muted);padding:13px 18px;font-weight:300}
.submit{position:absolute;left:157px;top:408px;width:152px;height:42px}
.info{position:absolute;left:852px;display:flex;gap:12px;align-items:flex-start}
.info .ico{width:32px;height:32px;flex:none}
.info small{display:block;font-size:12px}
.info span{display:block;font-size:14.5px;color:var(--brown)}
.info strong{display:block;font-size:24px;font-weight:400;color:var(--brown)}
.swoosh{position:absolute;right:-60px;bottom:-60px;width:240px;height:240px;border-radius:50%;background:#efe3d4}

/* footer */
.site-footer{height:415px}
.footer-brand{position:absolute;left:157px;top:86px;width:154px;height:170px;display:flex;flex-direction:column;align-items:center;justify-content:flex-end}
.footer-brand .ring{width:120px;height:120px;border-radius:50%;background:#f1ebe2;margin-bottom:10px}
.footer-links{position:absolute;left:441px;top:86px;list-style:none;font-size:12px;letter-spacing:2px;line-height:30px;text-transform:uppercase}
.sponsor{position:absolute;left:676px;top:87px;width:366px;height:108px;border:2px solid #ececec;border-radius:10px;text-align:center}
.sponsor-label{position:absolute;top:-9px;left:50%;transform:translateX(-50%);background:var(--white);padding:0 10px;font-size:12px;letter-spacing:2.5px;color:var(--brown);white-space:nowrap}
.sponsor-name{position:absolute;left:80px;top:29px;width:204px;height:62px;display:flex;align-items:center;justify-content:center;font-size:30px;font-weight:500;color:#1e2a6b}
.accredit{position:absolute;left:676px;top:222px;width:296px;height:32px;border-radius:3px;background:#d9dcea}
.contact-row{position:absolute;top:334px;left:0;width:1200px;display:flex;justify-content:center;align-items:center}
.contact-row .item{display:flex;align-items:center;gap:12px;padding:0 36px}
.contact-row .item + .item{border-left:1px solid var(--rule)}
.contact-row .ico{width:32px;height:32px}
.contact-row small{display:block;font-size:12px}
.contact-row span{display:block;font-size:14px;color:var(--brown)}
.bottom-bar{position:absolute;top:4158px;left:0;width:1200px;height:47px;background:var(--night);color:#bfc3c8;font-size:11px}
.bottom-bar p{position:absolute;left:157px;top:17px}
.socials{position:absolute;left:950px;top:13px;display:flex;gap:12px}
.socials i{width:21px;height:21px;border-radius:50%;border:1px solid #9ea3a9;display:block}
</style>
</head>
<body>

<header class="hero">
  <div class="hero-photo" role="img" aria-label="Two-storey house with grey cladding, dark roof, garden beds and a balustrade fence"></div>
  <div class="hero-shade"></div>
  <nav class="nav nav-left"><span>HOME</span><span>SERVICES</span><span>GALLERY</span><span>ABOUT</span></nav>
  <nav class="nav nav-right"><span>CONTACT</span><span>ALL TESTIMONIALS</span></nav>
  <span class="ico nav-phone"><svg viewBox="0 0 24 24" fill="none" stroke="currentColor" stroke-width="2"><path d="M5 3h4l2 5-3 2a12 12 0 0 0 6 6l2-3 5 2v4a2 2 0 0 1-2 2A17 17 0 0 1 3 5a2 2 0 0 1 2-2z"/></svg></span>
  <div class="brand-badge"><span class="brand-name">Kestrel Painters</span></div>
  <h1 class="hero-title">Always on Target</h1>
  <p class="hero-text">We strive to ensure the highest quality paint-work, paying close attention<br>to detail to provide a long lasting finish.</p>
  <span class="btn btn-light">Request a Quote</span>
</header>

<section class="services">
  <h2 class="section-title abs" style="top:70px;width:100%">We service Hamilton, Cambridge, Te Awamutu<br>and the broader Waikato region.</h2>
  <p class="lead abs" style="top:174px;width:100%">We understand that arranging painters and fitting into building schedules can be difficult. We work to provide<br>a stress-free, seamless decorating service to make sure your project runs as smoothly as possible.</p>

  <div class="service" style="left:132px;top:277px"><div class="service-photo" role="img" aria-label="Painter on a ladder coating exterior weatherboards" style="background:linear-gradient(160deg,#3f79c2,#b9c3cc 55%,#4d4e55)"></div><p class="service-name">Exterior Painting</p></div>
  <div class="service" style="left:451px;top:277px"><div class="service-photo" role="img" aria-label="Freshly painted empty room with timber floor" style="background:linear-gradient(180deg,#d9d3c7,#a9c1bd 55%,#6e4a33)"></div><p class="service-name">Interior Painting</p></div>
  <div class="service" style="left:769px;top:277px"><div class="service-photo" role="img" aria-label="Lounge with a sofa in front of a patterned feature wall" style="background:linear-gradient(180deg,#ececec,#d8d8d8 60%,#9a9a9a)"></div><p class="service-name">Wallpapering</p></div>

  <div class="service" style="left:132px;top:612px"><div class="service-photo" role="img" aria-label="Plasterer smoothing a wall with a trowel" style="background:linear-gradient(150deg,#f2f2f2,#dcdcdc 60%,#b8b8b8)"></div><p class="service-name">Plastering</p></div>
  <div class="service" style="left:451px;top:612px"><div class="service-photo" role="img" aria-label="Clean suburban home with a double garage" style="background:linear-gradient(180deg,#bcd3e6,#e8e4dc 55%,#8a8a84)"></div><p class="service-name">Waterblasting &amp; House<br>Cleaning</p></div>
  <div class="service" style="left:769px;top:612px"><div class="service-photo" role="img" aria-label="Worker spray-painting a red roof" style="background:linear-gradient(160deg,#f4f4f4,#5d77a8 45%,#b65b4a)"></div><p class="service-name">Roof Painting</p></div>

  <span class="btn learn" style="top:826px">Learn More</span>
</section>

<section class="pride">
  <div class="pride-photo" role="img" aria-label="Rendered house with grey roof and lawn after repainting"></div>
  <div class="pride-copy">
    <h2>We take a lot of pride in<br>our work.</h2>
    <p>We strive to ensure the highest quality paint-work, paying close attention to detail to provide a long lasting finish. Our clients are always our priority, we aim to deliver beyond their expectations. It is our goal to provide an excellent service from start to finish through clear communication, free quoting and transparency with our pricing.</p>
    <p>We take great pride in the preparation of surfaces for painting and only use the best quality products to ensure we achieve the best finish for you.</p>
    <div class="call" style="gap:30px;margin-top:34px">
      <span class="btn btn-brown" style="width:150px;height:42px">About Us</span>
      <div class="call">
        <span class="ico"><svg viewBox="0 0 24 24" fill="none" stroke="currentColor" stroke-width="2"><path d="M5 3h4l2 5-3 2a12 12 0 0 0 6 6l2-3 5 2v4a2 2 0 0 1-2 2A17 17 0 0 1 3 5a2 2 0 0 1 2-2z"/></svg></span>
        <div><small>Call Us At</small><strong>022 555 0147</strong></div>
      </div>
    </div>
  </div>
</section>

<section class="feedback">
  <h2 class="section-title">Valuable Feedback from our Customers</h2>
  <svg class="abs" style="left:120px;top:263px" width="24" height="16" viewBox="0 0 24 16" fill="none" stroke="#d8c6ad" stroke-width="2"><path d="M23 8H2M8 1 1 8l7 7"/></svg>
  <article class="quote-card" style="left:157px">
    <span class="quote-mark"><svg width="18" height="14" viewBox="0 0 18 14" fill="#8a6a45"><path d="M0 14V8c0-4 2-7 6-8l1 2c-2 1-3 3-3 5h3v7zm10 0V8c0-4 2-7 6-8l1 2c-2 1-3 3-3 5h3v7z"/></svg></span>
    <p>We could not be happier with the work done painting the exterior of our two storey home. Sam and Theo had brilliant communication and the job went very smoothly. Would definitely recommend!</p>
    <cite><b>CLARA WHITFIELD</b> (2020)</cite>
  </article>
  <article class="quote-card" style="left:615px">
    <span class="quote-mark"><svg width="18" height="14" viewBox="0 0 18 14" fill="#8a6a45"><path d="M0 14V8c0-4 2-7 6-8l1 2c-2 1-3 3-3 5h3v7zm10 0V8c0-4 2-7 6-8l1 2c-2 1-3 3-3 5h3v7z"/></svg></span>
    <p>Great job, very happy. Thanks Sam!!<br>Lorem ipsum dolor sit amet, consectetur adipiscing elit, sed do eiusmod tempor incididunt ut labore et dolore magna aliqua.</p>
    <cite><b>OWEN</b> (AUGUST, 2017)</cite>
  </article>
  <svg class="abs" style="left:1056px;top:263px" width="24" height="16" viewBox="0 0 24 16" fill="none" stroke="#e8dcc9" stroke-width="2"><path d="M1 8h21M16 1l7 7-7 7"/></svg>
</section>

<section class="projects">
  <h2>Check out our recent projects</h2>
  <div class="arrows">
    <svg width="24" height="16" viewBox="0 0 24 16" fill="none" stroke="#2b2b2b" stroke-width="2"><path d="M23 8H2M8 1 1 8l7 7"/></svg>
    <svg width="24" height="16" viewBox="0 0 24 16" fill="none" stroke="#c9b293" stroke-width="2"><path d="M1 8h21M16 1l7 7-7 7"/></svg>
  </div>
  <div class="project" role="img" aria-label="Bright kitchen and dining area with white cabinets" style="left:0;width:387px;background:linear-gradient(180deg,#e9e6df,#cfc8bb 55%,#6a3b22)"></div>
  <div class="project" role="img" aria-label="Modern grey home with brick path under blue sky" style="left:407px;width:387px;background:linear-gradient(180deg,#2f6fc0,#89b0d8 40%,#6e7269 65%,#5a5d5e)">
    <svg class="abs" style="right:18px;top:18px" width="24" height="24" viewBox="0 0 24 24" fill="none" stroke="#fff" stroke-width="2.2"><circle cx="10" cy="10" r="7"/><path d="m15 15 7 7"/></svg>
  </div>
  <div class="project" role="img" aria-label="Repainted grey weatherboard house with dark base" style="left:813px;width:387px;background:linear-gradient(180deg,#c9d8e8,#9aa3ab 50%,#3e4245 85%)"></div>
</section>

<section class="enquiry">
  <div class="swoosh"></div>
  <p class="kicker">Need Help?</p>
  <h2>Schedule A Services</h2>
  <p class="intro">We work to provide a stress-free, seamless decorating service to make sure your project runs as smoothly as possible. We maintain a clean and safe work-space at all times and are happy to work around you, your family, staff or tenants.</p>
  <div class="field" style="left:157px;top:227px;width:315px;height:44px">Name*</div>
  <div class="field" style="left:157px;top:287px;width:315px;height:44px">Email*</div>
  <div class="field" style="left:157px;top:346px;width:315px;height:44px">Location*</div>
  <div class="field" style="left:487px;top:227px;width:313px;height:163px">Message*</div>
  <span class="btn btn-brown submit">Submit</span>
  <div class="info" style="top:232px">
    <span class="ico"><svg viewBox="0 0 24 24" fill="none" stroke="currentColor" stroke-width="2"><path d="M5 3h4l2 5-3 2a12 12 0 0 0 6 6l2-3 5 2v4a2 2 0 0 1-2 2A17 17 0 0 1 3 5a2 2 0 0 1 2-2z"/></svg></span>
    <div><small>Call Us At</small><strong>022 555 0147</strong></div>
  </div>
  <div class="info" style="top:295px">
    <span class="ico"><svg viewBox="0 0 24 24" fill="none" stroke="currentColor" stroke-width="2"><rect x="3" y="5" width="18" height="14" rx="2"/><path d="m3 7 9 6 9-6"/></svg></span>
    <div><small>Email</small><span>hello@kestrelpainters.co.nz</span></div>
  </div>
  <div class="info" style="top:357px">
    <span class="ico"><svg viewBox="0 0 24 24" fill="none" stroke="currentColor" stroke-width="2"><path d="M12 22s7-7 7-12a7 7 0 0 0-14 0c0 5 7 12 7 12z"/><circle cx="12" cy="10" r="2.5"/></svg></span>
    <div><small>Address</small><span>Harbourview, Waikato.</span></div>
  </div>
</section>

<footer class="site-footer">
  <div class="footer-brand"><div class="ring"></div><span class="brand-name">Kestrel Painters</span></div>
  <ul class="footer-links"><li>Home</li><li>Services</li><li>Gallery</li><li>About</li><li>Contact</li><li>All Testimonials</li></ul>
  <div class="sponsor">
    <span class="sponsor-label">PROUDLY SPONSORED BY</span>
    <span class="sponsor-name">Veltora</span>
  </div>
  <div class="accredit" role="img" aria-label="Accredited painter badge"></div>
  <div class="contact-row">
    <div class="item">
      <span class="ico"><svg viewBox="0 0 24 24" fill="none" stroke="currentColor" stroke-width="2"><path d="M5 3h4l2 5-3 2a12 12 0 0 0 6 6l2-3 5 2v4a2 2 0 0 1-2 2A17 17 0 0 1 3 5a2 2 0 0 1 2-2z"/></svg></span>
      <div><small>Call Us At</small><span>022 555 0147</span></div>
    </div>
    <div class="item">
      <span class="ico"><svg viewBox="0 0 24 24" fill="none" stroke="currentColor" stroke-width="2"><rect x="3" y="5" width="18" height="14" rx="2"/><path d="m3 7 9 6 9-6"/></svg></span>
      <div><small>Email</small><span>hello@kestrelpainters.co.nz</span></div>
    </div>
    <div class="item">
      <span class="ico"><svg viewBox="0 0 24 24" fill="none" stroke="currentColor" stroke-width="2"><path d="M12 22s7-7 7-12a7 7 0 0 0-14 0c0 5 7 12 7 12z"/><circle cx="12" cy="10" r="2.5"/></svg></span>
      <div><small>Address</small><span>Harbourview, Waikato.</span></div>
    </div>
  </div>
</footer>

<div class="bottom-bar">
  <p>© Copyright 2022 Kestrel Painters. All rights reserved.</p>
  <div class="socials"><i></i><i></i><i></i></div>
</div>

</body>
</html>
```